Website Design for new skincare product launch/rebranding

The Dew Meridian website is currently live and built through Pagevolt.com. While the existing site has served as a strong starting point, I’m now looking to elevate the overall experience with a complete redesign that reflects the growth and vision of the brand. This will be a full visual and functional revamp — not just a refresh — with the goal of creating a more elevated, intuitive, and conversion-focused platform. I’m looking for a designer who can not only reimagine the layout and visuals, but also collaborate on optimizing the user journey and site structure for both storytelling and sales.

Target Market(s)

Age 25- 45 (core), with secondary appeal to 18-55. Primarily women, but gender inclusive. Wellness/Holistic Beauty/Organic Ingredients, Botanical.

Industry/Entity Type

Beauty, aesthetics, wellness.

Number of Pages Required

5+ page

Font styles to use
Other font styles liked:
• Gravesned Sans Family

Colors

Designer to choose colors to be used in the design.

Requirements
Must have
• Include standard pages (Home, Our Story/Values, Shop, Product Detail with ingredients/description/etc., Contact) and any other recommended sections to optimize conversion. Minimal, clean, calming visual. Seamlessly integrate with Cartwell for all product sales.
Nice to have
• Company colors are attached in images, along with first two products that are launching. One called Velunmist, and one called Petravelle. Fonts and shapes need to align accordingly. Feel elevated, neutral, and luxe while maintaining a grounded, earthy minimalism. Visual inspiration includes brands like Lantern Grove, Marble Osprey, and TOvelin — minimal yet high-end, with thoughtful use of whitespace, typography, and subtle movement. Would LOVE to have movement (short clip GIF) on either the home page or ingredient page, reference TOvelin website (homepage or LuminWeave System™ Tab)
Should not have
• dark colors, complex design elements, too many different fonts. For ingredients, stick to botanical images and information only, with no mentions of CBD or use of leaf imagery.

```html
<!DOCTYPE html>
<html lang="en">
<head>
<meta charset="utf-8">
<title>Dew Meridian — Elevate Your Skin, Naturally</title>
<link rel="stylesheet" href="https://fonts.googleapis.com/css2?family=Questrial&family=Poppins:wght@400;500;600&display=swap">
<style>
:root{
  --ink:#161616;
  --text:#3a3a3a;
  --muted:#6f6f6f;
  --stone:#a4a39b;
  --stone-dark:#8f8e86;
  --hero-a:#ece7e2;
  --hero-b:#d9d1c9;
  --band:#e9e4dc;
  --line:#e2e0dc;
  --white:#ffffff;
  --accent:#c98a8a;
}
*{box-sizing:border-box;margin:0;padding:0}
html,body{width:1200px;height:4280px;overflow:hidden;background:var(--white)}
body{position:relative;font-family:"Poppins",sans-serif;color:var(--text)}
.abs{position:absolute}
.display{font-family:"Questrial",sans-serif;color:var(--ink);text-transform:uppercase;letter-spacing:.02em;font-weight:400}
.eyebrow{font-family:"Questrial",sans-serif;font-size:19px;color:var(--ink);text-transform:uppercase;letter-spacing:.04em}
.center{left:0;width:1200px;text-align:center}
.btn{position:absolute;background:linear-gradient(180deg,#b1b0a8,var(--stone-dark));color:var(--white);border-radius:40px;font-size:12px;letter-spacing:.08em;text-transform:uppercase;display:flex;align-items:center;justify-content:center;box-shadow:0 3px 6px rgba(0,0,0,.15)}

/* hero */
.hero{left:0;top:0;width:1200px;height:607px;background:radial-gradient(circle at 80% 20%,#f6f2ee 0,transparent 45%),linear-gradient(120deg,var(--hero-a),var(--hero-b))}
.logo{font-family:"Questrial",sans-serif;color:var(--ink);text-transform:uppercase;letter-spacing:.06em;display:flex;align-items:center;gap:8px}
.logo i{display:block;border:1.5px solid var(--ink);border-radius:50%}
.nav a{position:absolute;top:33px;font-size:13px;color:var(--ink);text-decoration:none}
.nav-icons{left:798px;top:32px;display:flex;gap:6px}
.nav-icons span{width:17px;height:17px;border-radius:50%;background:var(--stone-dark)}
.hero h1{left:150px;top:150px;font-size:57px;line-height:72px}
.hero p{left:150px;top:306px;width:400px;font-size:12.5px;line-height:21px;color:var(--ink)}
.price{left:150px;top:388px;font-family:"Questrial",sans-serif;font-size:19px;color:var(--ink);display:flex;gap:28px}
.price b{font-weight:400;color:var(--accent)}

/* story */
.photo{border-radius:14px}
.story-text{left:475px;top:826px;width:405px;font-size:12px;line-height:22.5px}

/* shop */
.product-stand{background:var(--stone);border-radius:6px}
.product-img{background:linear-gradient(180deg,#ececec,#bdbdbd);border-radius:14px 14px 10px 10px}
.stars{font-size:16px;letter-spacing:5px;color:#9a9a9a;text-align:center}
.pname{font-family:"Questrial",sans-serif;font-size:17px;letter-spacing:.12em;color:var(--ink);text-align:center}
.pprice{font-size:12px;letter-spacing:.12em;color:var(--ink);text-align:center}

/* benefits */
.band{left:0;top:1718px;width:1200px;height:606px;background:radial-gradient(ellipse at 50% 40%,#e3dbd2 0,transparent 55%),linear-gradient(180deg,#ebe7df,var(--band))}
.benefit{width:300px;text-align:center}
.benefit .ring{width:64px;height:64px;margin:0 auto;border:3px solid var(--stone-dark);border-radius:50%;display:flex;align-items:center;justify-content:center}
.benefit .dot{width:26px;height:26px;margin:22px auto 0;border-radius:50%;background:var(--stone-dark);border:4px solid #d6d3cc}
.benefit h3{margin-top:20px;font-family:"Questrial",sans-serif;font-weight:400;font-size:15px;color:var(--ink)}
.benefit p{margin-top:6px;font-size:10px;line-height:15px;color:var(--ink)}

/* faq */
.faq{background:var(--white);border:1.5px solid var(--line);border-radius:8px;box-shadow:0 2px 6px rgba(0,0,0,.06);display:flex;align-items:center;justify-content:space-between;padding:0 18px 0 14px;font-size:15px;line-height:22px;color:var(--muted)}
.faq .minus{width:12px;height:1.5px;background:var(--muted)}
.faq-open{background:var(--stone);border-radius:8px;color:var(--white);padding:14px 13px}
.faq-open h4{font-size:15px;font-weight:500;line-height:21px;width:250px}
.faq-open p{margin-top:12px;font-size:9px;line-height:16px}
.faq-open .more{margin-top:16px;font-size:11px;font-weight:600}
.faq-open .plus{position:absolute;right:14px;top:22px;font-size:20px;font-weight:300}

/* testimonial */
.quote-text{left:290px;top:3036px;width:620px;text-align:center;font-size:11.5px;line-height:22px;color:var(--ink)}
.arrow{width:34px;height:34px;border-radius:50%;display:flex;align-items:center;justify-content:center}

/* contact */
.field{border:1.5px solid var(--line);border-radius:8px;font-size:12px;color:var(--muted);padding:0 18px;display:flex;align-items:center;box-shadow:0 1px 4px rgba(0,0,0,.05)}

/* footer */
.footer{left:0;top:3869px;width:1200px;height:411px;background:radial-gradient(ellipse at 50% 30%,#ddd5cd 0,transparent 55%),linear-gradient(180deg,#ebe5df,#e2dbd3)}
.fcol h5{font-size:17px;font-weight:500;color:var(--ink);margin-bottom:14px}
.fcol a,.fcol span{display:block;font-size:14px;color:var(--ink);text-decoration:none;line-height:30px}
.small{font-size:11px;color:var(--ink)}
</style>
</head>
<body>

<!-- HERO -->
<section class="abs hero" role="img" aria-label="Soft blurred champagne bokeh backdrop with faint botanical line art"></section>
<div class="abs logo" style="left:150px;top:28px;font-size:22px"><i style="width:14px;height:14px"></i>Dew Meridian</div>
<nav class="nav">
  <a style="left:374px">Home</a><a style="left:449px">Our Story</a><a style="left:543px">Shop</a><a style="left:613px">Product Details</a>
</nav>
<div class="abs nav-icons"><span></span><span></span><span></span><span></span></div>
<div class="btn" style="left:891px;top:22px;width:161px;height:38px">Contact Us</div>

<h1 class="abs display hero-title" style="left:150px;top:150px;font-size:57px;line-height:72px">Elevate Your<br>Skin, Naturally</h1>
<p class="abs" style="left:150px;top:306px;width:400px;font-size:12.5px;line-height:21px;color:var(--ink)">Lorem Ipsum Dolor Sit Amet Consectetur. Pellentesque Luctus Eu Lorem Lorem Ipsum Dolor Sit Amet Consectetur. Pellentesque Luctus Eu Lorem..</p>
<div class="abs price"><span>Prices</span><b>|</b><span>$10.99</span></div>
<div class="btn" style="left:150px;top:449px;width:168px;height:38px">Add To Card</div>
<div class="abs" role="img" aria-label="Two grey dropper serum bottles standing on a marble and gold podium" style="left:640px;top:95px;width:415px;height:500px;background:radial-gradient(ellipse at 50% 45%,#b8b6b3 0,#a9a7a4 45%,transparent 70%),radial-gradient(ellipse at 50% 92%,#c9b27a 0,transparent 45%);border-radius:30px"></div>

<!-- OUR STORY -->
<div class="abs photo" role="img" aria-label="Woman applying serum with a dropper in a bright bathroom" style="left:150px;top:700px;width:287px;height:314px;background:linear-gradient(135deg,#c9c4c0,#efe9e4 55%,#d8d0c8)"></div>
<div class="abs eyebrow" style="left:475px;top:704px">Our Story</div>
<h2 class="abs display" style="left:475px;top:736px;width:600px;font-size:28px;line-height:38px">Where Nature Meets Nurture Our<br>Journey To Radiant Skin</h2>
<p class="abs story-text">Lorem Ipsum Dolor Sit Amet Consectetur. Feugiat Lorem Arcu Id Aliquet. Vulputate Quis Venenatis Viverra Libero Accumsan Odio Risus Enim. Morbi Feugiat Nibh Vel Sit Nisi Sit Rutrum Fermentum Non. Id Malesuada Tincidunt Sagittis Cum. Sagittis Velit Feugiat Adipiscing Porta Morbi Vel Aliquet. Odio Sem Massa Volutpat Proin Ipsum Sit. Bibendum Tristique Lectus</p>
<div class="btn" style="left:475px;top:974px;width:165px;height:38px">Learn More</div>
<div class="abs product-stand" style="left:921px;top:932px;width:134px;height:82px"></div>
<div class="abs product-img" role="img" aria-label="Grey dropper serum bottle with a pink floral sketch" style="left:955px;top:800px;width:66px;height:200px"></div>

<!-- SHOP -->
<div class="abs eyebrow center" style="top:1128px">Shop</div>
<h2 class="abs display center" style="top:1164px;font-size:27px">Discover Beauty, Rooted In Nature</h2>

<div class="abs product-stand" style="left:359px;top:1450px;width:188px;height:87px"></div>
<div class="abs product-img" role="img" aria-label="Botanical serum dropper bottle" style="left:398px;top:1255px;width:122px;height:275px"></div>
<div class="abs stars" style="left:359px;top:1549px;width:188px">★★★★★</div>
<div class="abs" style="left:379px;top:1579px;width:150px;height:1px;background:#8a8a8a"></div>
<div class="abs pname" style="left:309px;top:1592px;width:288px">Botanical Serum</div>
<div class="abs pprice" style="left:309px;top:1622px;width:288px">$38.00</div>

<div class="abs product-stand" style="left:656px;top:1450px;width:183px;height:87px"></div>
<div class="abs product-img" role="img" aria-label="White botanical balm stick" style="left:692px;top:1255px;width:112px;height:268px;background:linear-gradient(90deg,#e8e8ea,#fbfbfb 50%,#e2e2e4)"></div>
<div class="abs stars" style="left:656px;top:1549px;width:183px">★★★★★</div>
<div class="abs" style="left:672px;top:1579px;width:150px;height:1px;background:#8a8a8a"></div>
<div class="abs pname" style="left:605px;top:1592px;width:288px">Botanical Balm</div>
<div class="abs pprice" style="left:605px;top:1622px;width:288px">$38.00</div>

<!-- BENEFITS -->
<section class="abs band" role="img" aria-label="Faded portrait of a woman with soft skin behind pale botanical line art"></section>
<div class="abs eyebrow center" style="top:1821px">Benefits</div>
<h2 class="abs display center" style="top:1857px;font-size:27px">Pure Ingredients. Visible Results</h2>

<div class="abs benefit" style="left:185px;top:1957px">
  <div class="ring"><svg width="30" height="30" viewBox="0 0 30 30" fill="none" stroke="#8f8e86" stroke-width="2.4" stroke-linecap="round"><path d="M15 27V14"/><path d="M15 16c-6 0-9-4-9-9 6 0 9 4 9 9z"/><path d="M15 16c6 0 9-4 9-9-6 0-9 4-9 9z"/></svg></div>
  <div class="dot"></div>
  <h3>BOTANICAL-BASED FORMULAS</h3>
  <p>100% Plant-Powered, Skin-Friendly<br>Ingredients</p>
</div>
<div class="abs benefit" style="left:455px;top:1957px">
  <div class="ring"><svg width="30" height="30" viewBox="0 0 30 30" fill="none" stroke="#8f8e86" stroke-width="2.4" stroke-linecap="round"><circle cx="15" cy="15" r="10"/><path d="M10 15l4 4 7-8"/></svg></div>
  <div class="dot"></div>
  <h3>CLEAN &amp; NON-TOXIC</h3>
  <p>Safe And Effective For All Skin Types</p>
</div>
<div class="abs benefit" style="left:727px;top:1957px">
  <div class="ring"><svg width="30" height="30" viewBox="0 0 30 30" fill="none" stroke="#8f8e86" stroke-width="2.4" stroke-linejoin="round"><path d="M15 25S5 19 5 12a5 5 0 0 1 10-1 5 5 0 0 1 10 1c0 7-10 13-10 13z"/></svg></div>
  <div class="dot"></div>
  <h3>CRUELTY-FREE</h3>
  <p>Never Tested On Animals.</p>
</div>
<div class="btn" style="left:512px;top:2184px;width:188px;height:38px">Discover More</div>

<!-- FAQ -->
<div class="abs eyebrow center" style="top:2420px">Faqs</div>
<h2 class="abs display center" style="top:2457px;font-size:27px">Your Questions, Answered With Care</h2>

<div class="abs faq-open" style="left:150px;top:2558px;width:292px;height:206px">
  <h4>Lorem Ipsum Dolor Sit Amet Consectetur.</h4>
  <span class="plus">+</span>
  <p>Lorem Ipsum Dolor Sit Amet Consectetur. Varius Tincidunt In Parturient Tristique Enim Amet Lacus Quis Sed. Nulla Congue Purus In Lacus Risus Molestie.Lorem Ipsum Dolor Sit Amet Consectetur. Varius Tincidunt</p>
  <div class="more">Read More »</div>
</div>
<div class="abs faq" style="left:454px;top:2558px;width:292px;height:96px"><span>Lorem Ipsum Dolor Sit Amet<br>Consectetur.</span><i class="minus"></i></div>
<div class="abs faq" style="left:758px;top:2558px;width:292px;height:96px"><span>Lorem Ipsum Dolor Sit Amet<br>Consectetur.</span><i class="minus"></i></div>
<div class="abs faq" style="left:454px;top:2668px;width:292px;height:96px"><span>Lorem Ipsum Dolor Sit Amet<br>Consectetur.</span><i class="minus"></i></div>
<div class="abs faq" style="left:758px;top:2668px;width:292px;height:96px"><span>Lorem Ipsum Dolor Sit Amet<br>Consectetur.</span><i class="minus"></i></div>

<!-- TESTIMONIALS -->
<div class="abs eyebrow center" style="top:2858px">Testimonials</div>
<h2 class="abs display center" style="top:2894px;font-size:27px">Real Stories. Radiant Results</h2>

<svg class="abs" style="left:302px;top:2966px" width="56" height="42" viewBox="0 0 56 42" fill="#9a9993"><circle cx="13" cy="29" r="12"/><path d="M2 28C2 12 10 3 22 1l1 4C14 8 10 15 10 24z"/><circle cx="42" cy="29" r="12"/><path d="M31 28C31 12 39 3 51 1l1 4c-9 3-13 10-13 19z"/></svg>
<p class="abs quote-text">Lorem Ipsum Dolor Sit Amet Consectetur. Volutpat Nisi Eget Congue Velit Turpis Aliquet Auctor. Scelerisque Faucibus Ut Lobortis Blandit Orci Duis Sed. Sodales Viverra Tellus Pretium Morbi. Ut Sit Maecenas Convallis Eget Eget Libero Augue Placerat Faucibus.</p>
<div class="abs arrow" style="left:149px;top:3044px;background:var(--stone)"><svg width="12" height="12" viewBox="0 0 12 12" fill="none" stroke="#fff" stroke-width="1.8"><path d="M8 2L4 6l4 4"/></svg></div>
<div class="abs arrow" style="left:1016px;top:3044px;border:1.5px solid var(--ink)"><svg width="12" height="12" viewBox="0 0 12 12" fill="none" stroke="#161616" stroke-width="1.8"><path d="M4 2l4 4-4 4"/></svg></div>
<div class="abs center" style="top:3132px;font-size:19px;font-weight:500;color:var(--muted)">Elena Marsh</div>
<div class="abs center" style="top:3164px;font-size:10px;letter-spacing:.06em;color:var(--ink)">PROJEKTMANAGER</div>
<div class="abs" role="img" aria-label="Customer portrait" style="left:570px;top:3196px;width:70px;height:70px;border-radius:50%;background:linear-gradient(160deg,#cfc6bd,#8e7a68);border:3px solid #fff;box-shadow:0 2px 6px rgba(0,0,0,.2)"></div>
<svg class="abs" style="left:844px;top:3118px;transform:rotate(180deg)" width="56" height="42" viewBox="0 0 56 42" fill="#9a9993"><circle cx="13" cy="29" r="12"/><path d="M2 28C2 12 10 3 22 1l1 4C14 8 10 15 10 24z"/><circle cx="42" cy="29" r="12"/><path d="M31 28C31 12 39 3 51 1l1 4c-9 3-13 10-13 19z"/></svg>

<!-- CONTACT -->
<div class="abs eyebrow center" style="top:3362px">Contact Us</div>
<h2 class="abs display center" style="top:3398px;font-size:27px">We’re Here To Help — Let’s Connect</h2>
<form>
  <div class="abs field" style="left:211px;top:3482px;width:379px;height:48px">Fiest Name</div>
  <div class="abs field" style="left:607px;top:3482px;width:379px;height:48px">Last Name</div>
  <div class="abs field" style="left:211px;top:3542px;width:379px;height:48px">Phone Number</div>
  <div class="abs field" style="left:607px;top:3542px;width:379px;height:48px">Email</div>
  <div class="abs field" style="left:211px;top:3602px;width:775px;height:111px;align-items:flex-start;padding-top:16px">Messages</div>
  <div class="btn" style="left:213px;top:3736px;width:773px;height:37px">Submit</div>
</form>

<!-- FOOTER -->
<footer class="abs footer" role="img" aria-label="Faded portrait of a woman behind soft botanical line art"></footer>
<div class="abs logo" style="left:150px;top:4020px;font-size:30px"><i style="width:18px;height:18px"></i>Dew Meridian</div>
<p class="abs small" style="left:150px;top:4091px">Bringing You Peace Of Mind, One Wipe At A Time Your Hygiene, Our Promise From</p>
<div class="abs" style="left:150px;top:4150px;font-size:15px;color:var(--ink)">Enter You Emali</div>
<div class="abs" style="left:150px;top:4179px;width:141px;height:1px;background:var(--ink)"></div>
<div class="btn" style="left:518px;top:4142px;width:162px;height:38px">Subcribe</div>

<div class="abs fcol" style="left:716px;top:3966px">
  <h5>Product Details</h5>
  <a>My Account</a><a>Discount</a><a>Returns</a><a>Orders History</a><a>Order Tracking</a>
</div>
<div class="abs fcol" style="left:919px;top:3966px">
  <h5>Contact Us</h5>
  <span>Info@Dewmeridian.com</span><span>+(000)-0000-000</span><span style="line-height:22px;margin-top:4px">Lorem Ipsum<br>Dolor Sit Amet</span>
</div>
<div class="abs" style="left:150px;top:4238px;width:904px;height:1px;background:#bdb6ae"></div>
<div class="abs small" style="left:150px;top:4253px">Copyright © 2025 Dew Meridian - All Right Reserved</div>
<div class="abs small" style="left:828px;top:4253px">Terms Of Service</div>
<div class="abs small" style="left:974px;top:4253px">Privacy Policy</div>

</body>
</html>
```